Beyond The Ledger Double Sided DL Flyer

We need a double sided flyer that we provide to a Real Estate agent for leeds. It should provide our basic services as well as a modern look and feel. The brochure should incorporate our Brand colors and have a graphic that centres around money and property. I have included a couple of pictures that we like (but have not yet purchased from PIXVAULT) as an indication of the type of picture we like.

WE need to also show the Beyond The Ledger brand and have our Phone / address's and email details.

Target Market(s)

Realestate clients (Property Investors)

Industry/Entity Type

Financial Planning

Requirements
Must have
• Picture on Front (maybe the logo on back)
• Please incorporate existing logo colours.

```html
<!DOCTYPE html>
<html lang="en">
<head>
<meta charset="utf-8">
<title>Beyond The Ledger – DL Flyer</title>
<link rel="stylesheet" href="https://fonts.googleapis.com/css2?family=Fredoka:wght@600;700&family=Montserrat:wght@600;700;800&display=swap">
<style>
  :root {
    --brand-green: #8cc63f;
    --brand-black: #231f20;
    --paper: #ffffff;
    --ink: #1d1d1d;
    --canvas-bg: #e9eaeb;
    --photo-coins-a: #cfc8bd;
    --photo-coins-b: #7d756b;
    --photo-house-a: #eef0e8;
    --photo-house-b: #c9cfbf;
  }
  * { box-sizing: border-box; margin: 0; padding: 0; }
  html, body {
    width: 1200px; height: 1200px; overflow: hidden;
    background: var(--canvas-bg);
  }
  .stage {
    position: relative; width: 1200px; height: 1200px;
    display: flex; justify-content: center; align-items: center; gap: 60px;
  }
  .flyer {
    position: relative; width: 500px; height: 800px;
    background: var(--paper); overflow: hidden;
    box-shadow: 0 6px 18px rgba(0,0,0,.18);
  }
  .flyer-shapes { position: absolute; inset: 0; }

  /* ---------- back side ---------- */
  .photo-coins {
    position: absolute; left: 0; top: 140px; width: 500px; height: 250px;
    background: linear-gradient(160deg, var(--photo-coins-a) 0%, #a89f93 45%, var(--photo-coins-b) 100%);
  }
  .contact-block {
    position: absolute; top: 20px; left: 0; right: 0;
    text-align: center; color: var(--paper);
  }
  .contact-tel {
    font-family: "Fredoka", sans-serif; font-weight: 700;
    font-size: 36px; line-height: 40px; letter-spacing: 1.5px;
  }
  .contact-address {
    margin-top: 10px;
    font-family: "Montserrat", sans-serif; font-weight: 700;
    font-size: 11.5px; line-height: 16px; text-transform: uppercase;
  }
  .services-heading {
    position: absolute; top: 402px; left: 0; right: 0;
    text-align: center; color: var(--ink);
    font-family: "Fredoka", sans-serif; font-weight: 700;
    font-size: 23px; line-height: 25px; text-transform: uppercase; letter-spacing: .8px;
  }
  .service-list {
    position: absolute; top: 496px; left: 0; width: 500px; list-style: none;
  }
  .service-list li {
    height: 24px; margin-bottom: 8.5px; margin-left: 4px; margin-right: 28px;
    background: var(--brand-green); color: var(--ink);
    display: flex; align-items: center; justify-content: center;
    font-family: "Montserrat", sans-serif; font-weight: 700;
    font-size: 14.5px; text-transform: uppercase; letter-spacing: .4px;
  }
  .brand-name {
    font-family: "Montserrat", sans-serif; font-weight: 700;
    color: var(--brand-green); text-transform: uppercase;
  }
  .back-brand {
    position: absolute; top: 682px; left: 0; right: 0;
    text-align: center; font-size: 30px; line-height: 34px;
  }

  /* ---------- front side ---------- */
  .photo-house {
    position: absolute; left: 0; top: 0; width: 500px; height: 380px;
    background: radial-gradient(ellipse at 55% 45%, var(--photo-house-a) 0%, var(--photo-house-b) 60%, #9aa48e 100%);
  }
  .front-brand {
    position: absolute; top: 430px; left: 0; right: 0;
    text-align: center; font-size: 38px; line-height: 44px;
  }
  .front-footer {
    position: absolute; left: 0; right: 0; bottom: 0; height: 172px;
    background: var(--brand-black); color: var(--paper); text-align: center;
  }
  .front-tagline {
    margin-top: 18px;
    font-family: "Montserrat", sans-serif; font-weight: 600; font-size: 19px;
  }
  .front-cta {
    margin-top: 8px;
    font-family: "Fredoka", sans-serif; font-weight: 700; font-size: 40px;
    letter-spacing: 2px; text-transform: uppercase; line-height: 44px;
  }
  .front-phone {
    font-family: "Fredoka", sans-serif; font-weight: 700; font-size: 62px;
    line-height: 66px; color: var(--brand-green); letter-spacing: 1px;
  }
</style>
</head>
<body>
<main class="stage">

  <!-- Back side: contact and services -->
  <section class="flyer flyer-back">
    <div class="photo-coins" role="img" aria-label="Photo of a hand stacking coins on a wooden table"></div>
    <svg class="flyer-shapes" width="500" height="800" viewBox="0 0 500 800" aria-hidden="true">
      <path d="M0 0 H500 V105 C400 150 220 172 0 172 Z" fill="var(--brand-black)"/>
      <path d="M0 172 C220 172 400 150 500 105 V150 C400 190 220 214 0 218 Z" fill="var(--brand-green)"/>
      <path d="M0 390 C150 345 330 330 500 340 V800 H0 Z" fill="var(--brand-black)"/>
      <path d="M0 395 C150 355 330 345 500 355 V800 H0 Z" fill="var(--brand-green)"/>
      <path d="M0 420 C160 390 330 380 500 395 V800 H0 Z" fill="var(--paper)"/>
    </svg>
    <div class="contact-block">
      <p class="contact-tel">TEL. (02) 40001234</p>
      <p class="contact-address">5 / 18 Harbour View Rd Parkside NSW 2250<br>1 / 9 Lakeview Ave<br>Bayfield NSW 2263 (by appointment)</p>
    </div>
    <h2 class="services-heading">Accountants<br>and Financial Advisors<br>who specialise in:</h2>
    <ul class="service-list">
      <li>Negative Gearing &amp; Investment Properties</li>
      <li>Property &amp; Capital Gains Tax Minimisation</li>
      <li>Self-Managed Superannuation Funds (SMSF)</li>
      <li>Small Business &amp; Personal Taxation</li>
      <li>Investment Advice &amp; Risk Insurances</li>
    </ul>
    <p class="brand-name back-brand">Beyond<br>The Ledger</p>
  </section>

  <!-- Front side: picture and call to action -->
  <section class="flyer flyer-front">
    <div class="photo-house" role="img" aria-label="Photo of hands holding a small wooden house behind stacks of coins with green seedlings growing from them"></div>
    <p class="brand-name front-brand">Beyond<br>The Ledger</p>
    <div class="front-footer">
      <p class="front-tagline">Professional Accountants and Financial Advisors</p>
      <p class="front-cta">Call Now</p>
      <p class="front-phone">(02) 40001234</p>
    </div>
  </section>

</main>
</body>
</html>
```